Buff Works Business card design

i need a business card design for my new detailing company called 'Brent's Detail Shop'. i want an all black and white design . simple, direct and to the point. i want the designer to choose a fitting font to match the logothe front should have logo, address, phone and email and the back side should have a slogan and text indicating that we offer services on anything including cars, trucks, motorcycles and RVs. slogan will read "we take pride in your ride"
maybe also very small on the back side the IG icon with Brents_Detail_Shop

phone 208.474.2863
address 3847 E Larkmoor Ave
Spokane WA 98734
email: BrentsDetail@quorvamail.com

Target Market(s)

all ages , auto enthusiasts

Industry/Entity Type

Automotive

Contact Information for Business Card

the front should have logo, address, phone and email and the back side should have a slogan and text indicating that we offer services on anything including cars, trucks, motorcycles and RVs. slogan will read "we take pride in your ride"

phone 208.474.2863
address 3847 E Larkmoor Ave
Spokane WA 98734

Colors
000000
ffffff

Requirements
Must have
• bold font and very simple design with good spacing
Nice to have
• anything creative from the designer indicating we service any types of vehicles
Should not have
• any colors ,

```html
<!DOCTYPE html>
<html lang="en">
<head>
<meta charset="utf-8">
<title>Brent's Detail Shop – Business Card</title>
<link href="https://fonts.googleapis.com/css2?family=Lato:wght@400;700;900&display=swap" rel="stylesheet">
<style>
  :root {
    --ink: #0b0b0b;
    --paper: #f4f4f4;
    --white: #ffffff;
    --grey: #9a9a9a;
    --rule: #8a8a8a;
    --stage: #e6e3de;
    --accent: #3d6fa6;
  }
  * { margin: 0; padding: 0; box-sizing: border-box; }
  html, body { width: 1200px; height: 900px; overflow: hidden; }
  body {
    background: var(--stage);
    font-family: "Lato", Arial, sans-serif;
    position: relative;
  }
  .card {
    position: absolute;
    width: 560px;
    height: 320px;
    box-shadow: 0 10px 24px rgba(0,0,0,.22);
    overflow: hidden;
  }
  /* Back side */
  .card-back {
    left: 60px; top: 110px;
    background: var(--ink);
    color: var(--white);
    text-align: center;
    padding-top: 58px;
  }
  .services {
    font-size: 25px;
    line-height: 1.3;
    font-weight: 400;
    width: 340px;
    margin: 0 auto;
  }
  .divider {
    width: 350px;
    height: 1px;
    background: var(--rule);
    margin: 22px auto 18px;
  }
  .slogan {
    font-size: 20px;
    font-weight: 700;
    letter-spacing: .5px;
    text-transform: uppercase;
  }
  /* Front side */
  .card-front {
    left: 580px; top: 470px;
    background: var(--paper);
  }
  .wave { position: absolute; left: 0; top: 0; }
  .brand {
    position: absolute;
    left: 30px; top: 70px;
    width: 210px;
    display: flex;
    align-items: center;
    gap: 10px;
  }
  .brand-dot {
    width: 26px; height: 26px;
    border-radius: 50%;
    background: var(--ink);
    flex: none;
  }
  .brand-name {
    font-size: 26px;
    font-weight: 900;
    line-height: 1.1;
    color: var(--ink);
  }
  .contact {
    position: absolute;
    left: 300px; top: 42px;
    color: var(--ink);
    font-size: 15px;
    line-height: 1.35;
  }
  .contact-line { display: flex; align-items: center; gap: 4px; }
  .contact-line svg { flex: none; }
  .address { margin-top: 14px; margin-left: 18px; font-size: 16px; }
  .social {
    position: absolute;
    left: 320px; top: 238px;
    display: flex; align-items: center; gap: 7px;
    color: var(--white);
    font-size: 15px;
  }
  .social-dot {
    width: 18px; height: 18px; border-radius: 50%;
    background: var(--accent);
  }
</style>
</head>
<body>

<section class="card card-back">
  <p class="services">We offer services on anything including cars, trucks, motorcycles and RVs.</p>
  <div class="divider"></div>
  <p class="slogan">We take pride in your ride</p>
</section>

<section class="card card-front">
  <svg class="wave" width="560" height="320" viewBox="0 0 560 320">
    <path d="M0 320 L0 300 C120 300 260 250 330 200 C400 150 470 125 560 115 L560 320 Z" fill="var(--grey)"/>
    <path d="M0 320 L0 310 C140 312 270 265 340 212 C410 160 480 140 560 132 L560 320 Z" fill="var(--white)"/>
    <path d="M0 320 L0 318 C150 320 280 275 350 222 C420 172 490 152 560 146 L560 320 Z" fill="var(--ink)"/>
  </svg>

  <div class="brand">
    <span class="brand-dot"></span>
    <span class="brand-name">Brent's Detail Shop</span>
  </div>

  <div class="contact">
    <div class="contact-line">
      <svg width="14" height="12" viewBox="0 0 14 12"><path d="M1 4 C3 0 11 0 13 4 L10 5 L9 3 L5 3 L4 5 Z M3 6 H11 L12 11 H2 Z" fill="var(--ink)"/></svg>
      <span>208.474.2863</span>
    </div>
    <div class="contact-line">
      <svg width="14" height="10" viewBox="0 0 14 10"><rect x="0.5" y="0.5" width="13" height="9" fill="var(--ink)"/><path d="M1 1 L7 6 L13 1" stroke="var(--white)" fill="none"/></svg>
      <span>BrentsDetail@quorvamail.com</span>
    </div>
    <div class="address">
      3847 E Larkmoor Ave<br>
      Spokane WA 98734
    </div>
  </div>

  <div class="social">
    <span class="social-dot"></span>
    <span>Brents_Detail_Shop</span>
  </div>
</section>

</body>
</html>
```